Wedding Invite Location

We had my daughter's wedding invitations printed and mailed out before realizing we forgot to put the location of the wedding on the invitation. We would like to send out a postcard with the location to all who received an invitation

The pertinent information:

Melissa Hartwell and Gregory Blonsky

Grace Fellowship Church
27400 Wendle Rd.
Lakeview Harbor, MI 48093

Reception immediately following the service on the church grounds

```html
<!DOCTYPE html>
<html lang="en">
<head>
<meta charset="utf-8">
<title>Wedding Place Postcard — Melissa Hartwell &amp; Gregory Blonsky</title>
<link rel="stylesheet" href="https://fonts.googleapis.com/css2?family=Allura&family=Josefin+Sans:wght@300;400&display=swap">
<style>
  :root {
    --page-bg: #e4e4e7;
    --card-top: #ffffff;
    --card-bottom: #e2e2e2;
    --ink: #1c1c1c;
    --rule: #9a9a9a;
    --monogram-fill: #d6d6d8;
    --card-shadow: rgba(0, 0, 0, 0.18);
  }
  * { box-sizing: border-box; margin: 0; padding: 0; }
  html, body {
    width: 1200px;
    height: 900px;
    overflow: hidden;
    background: var(--page-bg);
  }
  .sheet {
    position: relative;
    width: 1200px;
    height: 900px;
    display: flex;
    align-items: center;
    justify-content: center;
    gap: 40px;
  }
  .postcard {
    position: relative;
    width: 540px;
    height: 405px;
    background: linear-gradient(180deg, var(--card-top) 0%, var(--card-bottom) 100%);
    box-shadow: 0 4px 14px var(--card-shadow);
    color: var(--ink);
  }

  /* Front */
  .postcard--front {
    display: flex;
    flex-direction: column;
    align-items: center;
    text-align: center;
  }
  .monogram {
    background: radial-gradient(ellipse at center, var(--monogram-fill) 0%, rgba(214,214,216,0) 72%);
  }
  .postcard--front .monogram {
    width: 150px;
    height: 108px;
    margin-top: 30px;
  }
  .couple-names {
    font-family: "Allura", cursive;
    font-size: 17px;
    margin-top: 14px;
  }
  .headline {
    font-family: "Allura", cursive;
    font-weight: 400;
    font-size: 60px;
    line-height: 1;
    margin-top: 30px;
  }
  .venue {
    font-family: "Josefin Sans", sans-serif;
    font-weight: 300;
    font-style: normal;
    font-size: 14.5px;
    line-height: 1.3;
    margin-top: 10px;
  }
  .reception-note {
    font-family: "Josefin Sans", sans-serif;
    font-weight: 300;
    font-size: 10px;
    margin-top: 42px;
  }

  /* Back */
  .stamp-box {
    position: absolute;
    top: 28px;
    right: 38px;
    width: 87px;
    height: 87px;
    border: 1px solid var(--rule);
  }
  .postcard--back .monogram {
    position: absolute;
    left: 68px;
    top: 168px;
    width: 160px;
    height: 100px;
  }
  .sender-line {
    position: absolute;
    left: 62px;
    top: 280px;
    width: 190px;
    font-family: "Allura", cursive;
    font-size: 17px;
    line-height: 1.1;
  }
  .address-lines {
    position: absolute;
    left: 285px;
    top: 186px;
    width: 200px;
  }
  .address-lines span {
    display: block;
    height: 1px;
    background: var(--rule);
    margin-bottom: 24px;
  }
</style>
</head>
<body>
<main class="sheet">
  <section class="postcard postcard--front" aria-label="Postcard front">
    <div class="monogram" role="img" aria-label="Couple's script monogram with flourishes"></div>
    <p class="couple-names">Melissa Hartwell &amp; Gregory Blonsky</p>
    <h1 class="headline">Wedding Place</h1>
    <address class="venue">
      Grace Fellowship Church<br>
      27400 Wendle Rd.<br>
      Lakeview Harbor, MI 48093
    </address>
    <p class="reception-note">Reception immediately following the service on the church grounds</p>
  </section>

  <section class="postcard postcard--back" aria-label="Postcard back">
    <div class="stamp-box" aria-hidden="true"></div>
    <div class="monogram" role="img" aria-label="Couple's script monogram with flourishes"></div>
    <p class="sender-line">Melissa Hartwell &amp;<br>Gregory Blonsky wedding</p>
    <div class="address-lines" aria-hidden="true">
      <span></span><span></span><span></span><span></span><span></span><span></span>
    </div>
  </section>
</main>
</body>
</html>
```